Graphic Designs for Website Slideshow Images

We need graphic designs of slideshow images to be used on our website https://www.vapelkin.com/

We have individual product images and would like to combine them by brand or collection to eye-catching slideshow images.

The ideal size of these images should be 1200 pixels wide by 800 pixels high. Designs should go with website (/www.vapelkin.com/) logo and theme.

Individual products shall be scaled to their true size (size info is widely available on the internet).

At least three designs are expected (one for each brand).

We're not just looking for designs but also designers we can work with for future projects.

Thanks for looking.

Project Deadline Extended
Reason: To provide additional product images.

Target Market(s)

Retail

Industry/Entity Type

Retail

Requirements
Must have
• At least one slideshow image for each brand: Brivane, Quorrel and Drifmoor
Should not have
• Copyrighted materials

```html
<!DOCTYPE html>
<html lang="en">
<head>
<meta charset="utf-8">
<title>Insulated Flasks – Only from £17.99</title>
<link rel="stylesheet" href="https://fonts.googleapis.com/css2?family=Big+Shoulders+Display:wght@500&family=Crimson+Pro:wght@700&display=swap">
<style>
  :root {
    --page-top: #d9d9d9;
    --page-mid: #f3f3f3;
    --page-bottom: #d4d4d4;
    --band-edge: #5d5a59;
    --band-mid: #a9a5a4;
    --brand-red: #8e2020;
    --label-text: #ffffff;
    --glow: rgba(255, 255, 255, 0.95);
  }
  * { box-sizing: border-box; margin: 0; padding: 0; }
  html, body { width: 1200px; height: 800px; overflow: hidden; }
  body { background: var(--page-top); }
  .slide {
    position: relative;
    width: 1200px;
    height: 800px;
    background: linear-gradient(180deg, var(--page-top) 0%, var(--page-mid) 22%, var(--page-top) 32%, var(--page-top) 73%, var(--page-mid) 82%, var(--page-bottom) 100%);
  }
  .headline {
    position: absolute;
    top: 0;
    left: 0;
    width: 1200px;
    height: 260px;
  }
  .headline-text {
    font-family: "Big Shoulders Display", "Arial Narrow", sans-serif;
    font-weight: 500;
    font-size: 118px;
    fill: var(--brand-red);
  }
  .product-band {
    position: absolute;
    top: 262px;
    left: 0;
    width: 1200px;
    height: 326px;
    background: linear-gradient(180deg, var(--band-edge) 0%, #8a8685 20%, var(--band-mid) 45%, #8d8988 70%, var(--band-edge) 100%);
    box-shadow: 0 4px 10px rgba(0,0,0,0.25);
  }
  .product {
    position: absolute;
    border-radius: 8px 8px 10px 10px;
    box-shadow: 0 0 10px 4px var(--glow);
  }
  .product--black { left: 120px; top: 63px; width: 60px; height: 215px;
    background: linear-gradient(90deg, #1c1c1c, #4a4a4a 45%, #1e1e1e); }
  .product--steel { left: 420px; top: 70px; width: 58px; height: 205px;
    background: linear-gradient(90deg, #6d6d6d, #c9c9c9 45%, #777); box-shadow: none; }
  .product--silver { left: 728px; top: 73px; width: 60px; height: 202px;
    background: linear-gradient(90deg, #9a9a9a, #f5f5f5 45%, #a8a8a8); }
  .product--pink { left: 1017px; top: 71px; width: 60px; height: 207px;
    background: linear-gradient(90deg, #b0206f, #ec5aae 45%, #b22271); }
  .saving {
    position: absolute;
    top: 614px;
    width: 213px;
    height: 51px;
    background: var(--brand-red);
    color: var(--label-text);
    font-family: "Crimson Pro", Georgia, serif;
    font-weight: 700;
    font-size: 22px;
    line-height: 1;
    letter-spacing: 0.04em;
    font-variant-numeric: oldstyle-nums;
    display: flex;
    align-items: center;
    justify-content: center;
    padding-bottom: 3px;
  }
  .saving--1 { left: 43px; }
  .saving--2 { left: 342px; }
  .saving--3 { left: 649px; }
  .saving--4 { left: 940px; }
</style>
</head>
<body>
  <main class="slide">
    <svg class="headline" viewBox="0 0 1200 260" aria-labelledby="headline-title">
      <title id="headline-title">Only from £17.99</title>
      <text class="headline-text" x="187" y="205" textLength="803" lengthAdjust="spacing">ONLY FROM £17.99</text>
    </svg>

    <section class="product-band">
      <div class="product product--black" role="img" aria-label="Black vacuum flask with yellow grip band"></div>
      <div class="product product--steel" role="img" aria-label="Stainless steel vacuum flask with lime grip band"></div>
      <div class="product product--silver" role="img" aria-label="Silver stainless travel mug with black flip lid"></div>
      <div class="product product--pink" role="img" aria-label="Pink stainless travel mug with purple flip lid"></div>
    </section>

    <p class="saving saving--1">Save £11.00</p>
    <p class="saving saving--2">Save £4.00</p>
    <p class="saving saving--3">Save £7.00</p>
    <p class="saving saving--4">Save £7.00</p>
  </main>
</body>
</html>
```